SkyvoraQ Business Cards and Stationary Design

Need a design for our business cards and stationary. I want to carry on the theme of the logo. I want the business cards to have a design on the back. I would like the business cards and the stationary to carry the same theme, design scheme, and branding

Target Market(s)

Airlines and Maintenance Facilities

Industry/Entity Type

Aviation

Contact Information for Business Card

Name
Position Title
Address: 4827 Tollbeck Lane, Fort Pierce, Florida, 34951
Office Number
Mobile Number
Email
Website

Font styles to use
Serif
Sans Serif

Colors

Designer to choose colors to be used in the design.

```html
<!DOCTYPE html>
<html lang="en">
<head>
<meta charset="utf-8">
<title>SkyvoraQ Business Cards</title>
<link rel="stylesheet" href="https://fonts.googleapis.com/css2?family=Jost:wght@400;500;600&display=swap">
<style>
  :root {
    --page: #ffffff;
    --navy-deep: #171c28;
    --navy: #0e2650;
    --navy-mid: #112d5a;
    --blue: #2a8fd6;
    --blue-ring: #1f6cc0;
    --silver: #dfe4ec;
    --white: #f4f6fa;
  }
  * { margin: 0; padding: 0; box-sizing: border-box; }
  html, body { width: 1200px; height: 1200px; overflow: hidden; background: var(--page); }
  body { position: relative; font-family: "Jost", sans-serif; }

  .card {
    position: absolute;
    top: 467px;
    width: 480px;
    height: 266px;
    overflow: hidden;
  }
  .card--front {
    left: 90px;
    background: linear-gradient(35deg, var(--navy-deep) 20%, var(--navy) 100%);
  }
  .card--info {
    left: 630px;
    background: linear-gradient(200deg, var(--navy) 0%, var(--navy-mid) 55%, #15264a 100%);
  }

  /* Front */
  .front__ring {
    position: absolute;
    right: -40px;
    top: 40px;
    width: 200px;
    height: 200px;
    border-radius: 50%;
    border: 16px solid var(--blue-ring);
    opacity: 0.85;
  }
  .front__wordmark {
    position: absolute;
    left: 78px;
    top: 114px;
    font-weight: 600;
    font-size: 36px;
    letter-spacing: 0.14em;
    color: var(--silver);
    line-height: 1;
  }

  /* Info side */
  .info__name {
    position: absolute;
    left: 30px;
    top: 46px;
    font-size: 15px;
    font-weight: 400;
    color: var(--white);
    line-height: 1;
  }
  .info__title {
    position: absolute;
    left: 30px;
    top: 68px;
    font-size: 8px;
    letter-spacing: 0.2em;
    color: var(--blue);
  }
  .contact {
    position: absolute;
    left: 30px;
    list-style: none;
    color: var(--blue);
    font-size: 9.5px;
    line-height: 1.3;
  }
  .contact li { display: flex; align-items: flex-start; gap: 10px; }
  .contact svg { width: 13px; height: 12px; flex: none; margin-top: 1px; }
  .contact--address { top: 130px; }
  .contact--lines { top: 169px; }
  .contact--lines li { margin-bottom: 4px; }

  .info__mark {
    position: absolute;
    left: 356px;
    top: 78px;
    width: 84px;
    height: 84px;
    border-radius: 50%;
    border: 7px solid var(--blue-ring);
  }
  .info__wordmark {
    position: absolute;
    left: 330px;
    top: 176px;
    width: 136px;
    text-align: center;
    font-weight: 600;
    font-size: 13px;
    letter-spacing: 0.2em;
    color: var(--blue);
  }
</style>
</head>
<body>

<section class="card card--front" aria-label="Business card front">
  <div class="front__ring"></div>
  <div class="front__wordmark">SKYVORAQ</div>
</section>

<section class="card card--info" aria-label="Business card back">
  <div class="info__name">John Doe</div>
  <div class="info__title">CHIEF MECHANIC</div>

  <ul class="contact contact--address">
    <li>
      <svg viewBox="0 0 12 12" fill="none" stroke="currentColor" stroke-width="0.9"><path d="M6 11 C3 7.5 2.5 6 2.5 4.5 A3.5 3.5 0 0 1 9.5 4.5 C9.5 6 9 7.5 6 11Z"/><circle cx="6" cy="4.5" r="1.2"/></svg>
      <span>4827 Tollbeck Lane, Fort Pierce,<br>Florida, 34951. USA</span>
    </li>
  </ul>

  <ul class="contact contact--lines">
    <li>
      <svg viewBox="0 0 14 12" fill="none" stroke="currentColor" stroke-width="0.9"><path d="M1 6 C1 3 13 3 13 6 L11 7 L9.5 5.5 H4.5 L3 7 Z"/></svg>
      <span>(772) 480 3619</span>
    </li>
    <li>
      <svg viewBox="0 0 12 12" fill="none" stroke="currentColor" stroke-width="0.9"><rect x="3.5" y="0.5" width="5" height="11" rx="0.8"/><line x1="5.3" y1="10" x2="6.7" y2="10"/></svg>
      <span>(772) 615 2087</span>
    </li>
    <li>
      <svg viewBox="0 0 14 12" fill="none" stroke="currentColor" stroke-width="0.9"><rect x="0.5" y="1.5" width="13" height="9"/><path d="M0.5 1.5 L7 7 L13.5 1.5"/></svg>
      <span>info@skyvoraq.com</span>
    </li>
    <li>
      <svg viewBox="0 0 12 12" fill="none" stroke="currentColor" stroke-width="0.9"><circle cx="6" cy="6" r="5.3"/><ellipse cx="6" cy="6" rx="2.3" ry="5.3"/><line x1="0.7" y1="6" x2="11.3" y2="6"/></svg>
      <span>www.skyvoraq.com</span>
    </li>
  </ul>

  <div class="info__mark"></div>
  <div class="info__wordmark">SKYVORAQ</div>
</section>

</body>
</html>
```